Tinker's Fox sports bar beer & food menu

We need a menu design for our gastropub sports bar in L.A.'s Sawtelle Neighborhood (Little Osaka). We have a full-bar (hard liquor, craft beer, wine and cocktails) . We have a lunch and dinner menu as well as a happy hour menu. On Sundays we have a seperate menu with brunch items. The design concept is a British pub type of sports bar. We're looking for something different from our existing menu design. Ideally something cleaner and more legible. It should mesh a simple, modern sensibility with the more traditional darkened pub style of our interior design.

You can check out our Venuvista page for photos of the interior/exterior:
https://www.venuvista.com/biz_photos/tinkers-fox-los-angeles?tab=interior

You can view our existing menu here:
https://www.venuvista.com/biz_photos/tinkers-fox-los-angeles?tab=menu

If there's an area of the design that can be a little more playful it's our highlighted event schedule so that the events will stand out.

Target Market(s)

Age of 25 and up. Sawtelle is a cultural hub that caters to a younger, moderately affluent crowd.

Industry/Entity Type

Sports Bar

Font styles to use
Sans Serif

Colors

Designer to choose colors to be used in the design.

Requirements
Must have
• Logo, highlighted event schedule (beer pong Monday, trivia Tuesday, taco Tuesday, whiskey Wednesday, karaoke Saturday). The menu should be easy to read in a darkened bar. We'll be printing on standard 8.5x11 in portrait.
Nice to have
• We're trying to have the menu take up as few pages as possible.
Should not have
• We're trying to have the menu take up as few pages as possible. Food photography isn't necessary. A cover isn't necessary. Please avoid clip art of food.

```html
<!DOCTYPE html>
<html lang="en">
<head>
<meta charset="UTF-8">
<title>Tinker's Fox Menu</title>
<link href="https://fonts.googleapis.com/css2?family=Montserrat:wght@400;500;600;700&family=Saira+Stencil+One&display=swap" rel="stylesheet">
<style>
:root{
  --backdrop:#e6cfae;
  --paper:#f4f4f1;
  --ink:#262626;
  --muted:#8d8d8d;
  --gold:#dba94a;
  --tan:#c7b18a;
  --rule:#d2d2cf;
  --frame:#d6c3a0;
}
*{box-sizing:border-box;margin:0;padding:0}
html,body{width:1200px;height:800px;overflow:hidden;background:var(--backdrop)}
body{font-family:'Montserrat',sans-serif;color:var(--ink);position:relative}
.page{position:absolute;top:34px;width:562px;height:732px;background:var(--paper);padding:22px 30px;overflow:hidden}
.page--left{left:34px}
.page--right{left:604px}
.brand{display:flex;align-items:center;justify-content:center;gap:8px;margin-bottom:14px}
.brand__mark{width:16px;height:16px;background:var(--gold)}
.brand__name{font-weight:600;font-size:19px;color:var(--ink);letter-spacing:.5px}
.columns{display:flex;gap:30px}
.col{flex:1;min-width:0}
.section-title{font-family:'Saira Stencil One',sans-serif;color:var(--tan);font-size:27px;line-height:.95;letter-spacing:3px;text-transform:uppercase;margin-bottom:12px}
.section-title small{display:block;font-size:17px;letter-spacing:4px}
.item{position:relative;padding:0 34px 6px 0;margin-bottom:7px;border-bottom:1px solid var(--rule)}
.item:last-child{border-bottom:none}
.item__name{font-weight:600;font-size:11.5px;letter-spacing:.3px}
.item__desc{font-size:8.6px;color:var(--muted);line-height:1.4;margin-top:2px}
.item__price{position:absolute;right:0;top:0;color:var(--gold);font-weight:600;font-size:12px}
.boxed{border:1px dashed var(--frame);padding:12px 14px 4px}
.flatbreads{margin-top:12px}
.addons{display:flex;gap:8px;font-size:10px;font-weight:600;margin:2px 0 10px;white-space:nowrap}
.addons span{color:var(--gold)}
.addons em{font-style:normal;color:var(--ink);font-weight:500}
.cup{position:absolute;right:0;top:0;font-size:9px;color:var(--gold);font-weight:600}
.side{display:flex;justify-content:space-between;font-weight:600;font-size:11px;padding:5px 0;border-bottom:1px solid var(--rule)}
.side span{color:var(--gold)}
.deserts{margin-top:12px}
.drinks{margin-top:12px}
.drinks__grid{display:grid;grid-template-columns:1fr 1fr;column-gap:16px}
.events{margin-top:10px;background:var(--ink);color:var(--paper);padding:12px 14px 10px}
.events__title{font-family:'Saira Stencil One',sans-serif;color:var(--gold);font-size:21px;letter-spacing:3px;text-transform:uppercase;line-height:1;margin-bottom:8px}
.event{display:flex;align-items:center;gap:10px;font-size:10.5px;font-weight:600;padding:3px 0}
.event__day{width:36px;text-align:center;background:var(--gold);color:var(--ink);font-size:9px;font-weight:700;letter-spacing:1px;padding:2px 0}
</style>
</head>
<body>

<section class="page page--left">
  <header class="brand"><span class="brand__mark"></span><span class="brand__name">Tinker's Fox</span></header>
  <div class="columns">
    <div class="col">
      <h2 class="section-title">Burgers <small>and</small>Sandwiches</h2>
      <div class="item"><div class="item__name">Turkey Club Sandwich</div><div class="item__desc">Turkey Breast, Applewood Bacon, Butter Lettuce, White Cheddar, Avocado and Tomato Served on Sourdough Bread</div><div class="item__price">$12</div></div>
      <div class="item"><div class="item__name">Buttermilk Fried Chicken</div><div class="item__desc">Coleslaw, Provolone, Tomato, and a Spiced Mayonnaise on a Pretzel Roll</div><div class="item__price">$13</div></div>
      <div class="item"><div class="item__name">Short Rib Sandwich</div><div class="item__desc">Braised Shorts, Mayo, Tomato, Caramelized Onions, Arugula, Pepper Jack Cheese Served on Sourdough Bread</div><div class="item__price">$13</div></div>
      <div class="item"><div class="item__name">Grilled Cheese Sandwich</div><div class="item__desc">Swiss Cheese, Provolone and Cheddar Cheese</div><div class="item__price">$10</div></div>
      <div class="item"><div class="item__name">Tinker's Fox Burger</div><div class="item__desc">Sharp Cheddar, Arugula, Roasted Shallots, Bacon Jam with Malt Aioli</div><div class="item__price">$14</div></div>
      <div class="item"><div class="item__name">The Truffle Burger</div><div class="item__desc">Caramelized Onions, Arugula, Truffle Pecorino, Truffle Mayo and Truffle Fries</div><div class="item__price">$15</div></div>
      <div class="item"><div class="item__name">The Sloppy Joe</div><div class="item__desc">Shredded Lettuce with Sharp Cheddar</div><div class="item__price">$10</div></div>
      <div class="item"><div class="item__name">Veggie Burger</div><div class="item__desc">House Patty, Avocado and Pepper Cheddar</div><div class="item__price">$12</div></div>
      <div class="events">
        <h2 class="events__title">Weekly Events</h2>
        <div class="event"><span class="event__day">MON</span>Beer Pong Monday</div>
        <div class="event"><span class="event__day">TUE</span>Trivia Tuesday</div>
        <div class="event"><span class="event__day">TUE</span>Taco Tuesday</div>
        <div class="event"><span class="event__day">WED</span>Whiskey Wednesday</div>
        <div class="event"><span class="event__day">SAT</span>Karaoke Saturday</div>
      </div>
    </div>
    <div class="col">
      <h2 class="section-title">Big Dog<br>Bites</h2>
      <div class="item"><div class="item__name">Atlantic Cod Fish N' Chips</div><div class="item__desc">House Tartar Sauce, Vinegar and Lemon Wedge</div><div class="item__price">$16</div></div>
      <div class="item"><div class="item__name">Oven Roasted ½ Roasted Chicken</div><div class="item__desc">Boneless Chicken, Broccolini, Fingerling Potatoes Topped with Chimichurri Sauce</div><div class="item__price">$18</div></div>
      <div class="item"><div class="item__name">Black Mussels</div><div class="item__desc">Tequila Chipotle Sauce, Cilantro and Cherry Tomatoes</div><div class="item__price">$17</div></div>
      <div class="item"><div class="item__name">Pan Seared Salmon</div><div class="item__desc">Sushi Grade Salmon, Spaghetti Squash, Zucchini, Cherry Tomatoes In a Lemon Caper Beurre Blanc</div><div class="item__price">$21</div></div>
      <div class="item"><div class="item__name">Flat Iron Steak</div><div class="item__desc">French Fries, Baby Arugula in a Light peppercorn Sauce</div><div class="item__price">$22</div></div>
      <div class="flatbreads boxed">
        <h2 class="section-title">Flatbreads</h2>
        <div class="item"><div class="item__name">Margherita</div><div class="item__desc">Fresh Mozzarella, Roma Tomatoes and Fresh Italian Basil</div><div class="item__price">$12</div></div>
        <div class="item"><div class="item__name">Vegetarian</div><div class="item__desc">Brussel Sprouts, Peppers, Onions, Zucchini, Goat Cheese, Smoked Mozzarella Topped with a Balsamic Reduction</div><div class="item__price">$13</div></div>
        <div class="item"><div class="item__name">Prosciutto &amp; Arugula</div><div class="item__desc">Fig Jam, Parmesan, Mozzarella</div><div class="item__price">$14</div></div>
      </div>
    </div>
  </div>
</section>

<section class="page page--right">
  <header class="brand"><span class="brand__mark"></span><span class="brand__name">Tinker's Fox</span></header>
  <div class="columns">
    <div class="col">
      <div class="boxed">
        <h2 class="section-title"><small>For the</small>Table</h2>
        <div class="item"><div class="item__name">Tinker's 3 Whole Wings</div><div class="item__desc">Choice of Dry Rub, Sweet N' Spicy or Buffalo</div><div class="item__price">$9</div></div>
        <div class="item"><div class="item__name">Brussel Sprouts</div><div class="item__desc">Sautéed with Chorizo, Roasted Almonds and Golden Raisins</div><div class="item__price">$8</div></div>
        <div class="item"><div class="item__name">Golden Calamari</div><div class="item__desc">Traditionally Served with Spiced Marinara</div><div class="item__price">$11</div></div>
        <div class="item"><div class="item__name">Shrimp Mac N' Cheese</div><div class="item__desc">Baked with Fontina, Sharp Cheddar and Parmesan</div><div class="item__price">$12</div></div>
        <div class="item"><div class="item__name">½ Dozen Oysters</div><div class="item__desc">Cedar Cove's Served with Our Own Mignonette</div><div class="item__price">$12</div></div>
        <div class="item"><div class="item__name">Charcuterie</div><div class="item__desc">Seasonal Meats and Cheese</div><div class="item__price">$15</div></div>
        <div class="item"><div class="item__name">Nachos</div><div class="item__desc">Medley of Black Beans, Pico De Gallo, Cheese, Jalapeño and Sour Cream</div><div class="item__price">$9</div></div>
        <div class="item"><div class="item__name">Mozzarella Cheese Ctick</div><div class="item__price">$12</div></div>
      </div>
      <div class="deserts">
        <h2 class="section-title">Deserts</h2>
        <div class="side">Flan <span>$9</span></div>
        <div class="side">Bread Pudding <span>$9</span></div>
        <div class="side">Brownie Sundae <span>$9</span></div>
      </div>
    </div>
    <div class="col">
      <h2 class="section-title">Salads<small>and</small>Soups</h2>
      <div class="item"><div class="item__name">Chili Soupe</div><div class="item__desc">Turkey with Vegetables, Onions and Sharp Cheddar</div><div class="cup">Cup $5 | Bowl $8</div></div>
      <div class="item"><div class="item__name">Soup of the day</div><div class="item__desc">Romaine Hearts, Croutons and Shaved Parmesan</div><div class="cup">Cup $4 | Bowl $7</div></div>
      <div class="item"><div class="item__name">Tinker's Fox Chopped Salad</div><div class="item__desc">Romaine, Salami, Provolone, Banana Peppers, Red Onions, Olives, Garbanzos Tomatoes, Celery. Tossed in a Red Wine Vinaigrette</div><div class="item__price">$14</div></div>
      <div class="item"><div class="item__name">Southwest Salad</div><div class="item__desc">Romaine, Tomato, Corn, Avocado. Tossed with a Jalapeño Cilantro Vinaigrette Garnished with Tortilla Chips, Cheddar and Sour Cream</div><div class="item__price">$13</div></div>
      <div class="item"><div class="item__name">Quinoa Salad</div><div class="item__desc">Roasted Beets, Asparagus, Brussel Sprouts, Mushrooms, Kale, Watermelon Radish Tossed in a Citrus Vinaigrette</div><div class="item__price">$13</div></div>
      <div class="addons"><em>Add Ons:</em> Chicken <span>$4</span> Shrimp <span>$6</span> Salmon <span>$8</span></div>
      <h2 class="section-title">Sides</h2>
      <div class="side">House Fries <span>$5</span></div>
      <div class="side">Dry Rub Fries <span>$5</span></div>
      <div class="side">Truffle Fries <span>$7</span></div>
      <div class="side">Sweet Potato Fries <span>$6</span></div>
      <div class="drinks">
        <h2 class="section-title">Drinks</h2>
        <div class="drinks__grid">
          <div class="side">Craft Beer <span>$7</span></div>
          <div class="side">Wine <span>$10</span></div>
          <div class="side">Cocktails <span>$12</span></div>
          <div class="side">Whiskey <span>$9</span></div>
        </div>
      </div>
    </div>
  </div>
</section>

</body>
</html>
```